Larkfield Homecare - Website

MUST HAVE EXPERIENCE DESIGNING WEBSITES HEALTH CARE IN GENERAL AND/OR HOME NURSING SERVICES.

Details attached.

Number of Pages Required

1 page

Requirements
Must have
• Warm feel
caregivers

Color similar to the logo...

```html
<!DOCTYPE html>
<html lang="en">
<head>
<meta charset="utf-8">
<title>Larkfield Homecare</title>
<link href="https://fonts.googleapis.com/css2?family=Poppins:wght@400;500;600;700&family=Roboto:wght@400;500&display=swap" rel="stylesheet">
<style>
:root{
  --navy:#18225a;
  --orange:#f5891f;
  --teal:#15a1a8;
  --sky:#e7f4f5;
  --peach:#fdeee2;
  --grey:#7a7f8f;
  --red:#e23b3b;
  --green:#2aa07a;
  --line:#e6e8ec;
  --soft:#f7f7f8;
}
*{box-sizing:border-box;margin:0;padding:0}
html,body{width:1200px;height:4521px;overflow:hidden}
body{position:relative;background:#fff;font-family:'Poppins',sans-serif;color:var(--navy)}
.abs{position:absolute}
.btn-outline{position:absolute;border:2px solid var(--orange);color:var(--orange);border-radius:4px;font-size:11px;font-weight:600;display:flex;align-items:center;justify-content:center;letter-spacing:.3px}
.btn-fill{position:absolute;background:var(--orange);color:#fff;border-radius:3px;font-weight:600;display:flex;align-items:center;justify-content:center}
.section-title{position:absolute;font-size:31px;font-weight:500;display:flex;align-items:center;gap:18px}
.section-title::before{content:"";width:46px;height:3px;background:var(--orange)}
.brand{position:absolute;display:flex;align-items:center;gap:10px;font-weight:600;color:var(--teal)}
.brand .dot{border-radius:50%;background:var(--orange)}
.nav{position:absolute;left:309px;top:36px;display:flex;gap:22px;font-size:11.5px;font-weight:500;color:#555a6e}
.nav .active{color:var(--teal)}
.photo{position:absolute}
.form-card{position:absolute;left:144px;top:774px;width:359px;height:454px;background:#fff;border-radius:14px;box-shadow:0 10px 40px rgba(30,60,90,.08)}
.form-card h2{position:absolute;left:49px;top:56px;font-size:30px;font-weight:500}
.field{position:absolute;left:49px;width:265px;border-bottom:2px solid var(--line);height:48px}
.field b{display:block;font-size:13px;font-weight:600}
.field span{font-size:12px;color:#9da1ad;font-family:'Roboto',sans-serif}
.submit{position:absolute;left:49px;top:361px;width:265px;height:37px;background:var(--teal);color:#fff;font-weight:600;font-size:15px;border-radius:3px;display:flex;align-items:center;justify-content:center}
.about p{font-size:13.5px;line-height:20.5px;color:#6b6f7d;margin-bottom:12px}
.service-card{position:absolute;top:1619px;width:358px;height:263px;color:#fff;padding:48px 46px 0}
.service-card h3{font-size:19px;font-weight:700;line-height:21px;display:flex;gap:12px;align-items:center;margin-bottom:10px}
.service-card .ic{width:44px;height:44px;border:3px solid #fff;border-radius:50%;flex:none}
.service-card p{font-size:11px;line-height:17.5px}
.service-card .more{margin-top:14px;width:112px;height:28px;border:2px solid #fff;border-radius:3px;font-size:9.5px;font-weight:600;display:flex;align-items:center;justify-content:center}
.stat{position:absolute;top:2018px;text-align:center}
.stat small{display:block;font-size:12.5px;color:var(--grey)}
.stat strong{display:block;font-size:27px;font-weight:600;color:#444a5c;margin-top:2px}
.stat.o small,.stat.o strong{color:var(--orange)}
.stat.g small,.stat.g strong{color:var(--green)}
.stat.r small,.stat.r strong{color:var(--red)}
.team-card{position:absolute;top:2254px;width:246px;height:324px;background:#fff;border-radius:6px;box-shadow:0 6px 24px rgba(0,0,0,.07);overflow:hidden}
.team-card .pic{height:198px}
.team-card h4{margin:20px 0 0 26px;font-size:19px;font-weight:500}
.team-card p{margin:2px 0 0 26px;font-size:11.5px;color:var(--grey)}
.socials{display:flex;gap:14px;margin:10px 0 0 26px}
.socials i{width:12px;height:12px;border-radius:50%;background:#8a8f9c;display:block}
.news-big{position:absolute;left:89px;top:2722px;width:502px;height:570px;background:#fbfbfb;box-shadow:0 4px 16px rgba(0,0,0,.05)}
.meta{font-size:11.5px;color:#555;font-family:'Roboto',sans-serif}
.meta em{font-style:normal;border-left:1px solid #ccc;padding-left:10px;margin-left:10px}
.news-small{position:absolute;left:617px;width:492px;height:172px;background:#f6f6f6}
.news-small .thumb{position:absolute;left:16px;top:16px;width:183px;height:137px;border-radius:8px}
.news-small .txt{position:absolute;left:219px;top:44px;width:260px}
.news-small h5{font-family:'Roboto',sans-serif;font-size:16.5px;font-weight:500;line-height:30px;margin-top:12px}
footer h6{font-size:17px;font-weight:500;margin-bottom:10px}
footer li,footer .note{list-style:none;font-size:12px;color:#555a6e;line-height:22px}
.ring{display:block;width:24px;height:24px;border:1.5px solid #8a8f9c;border-radius:50%}
</style>
</head>
<body>

<svg class="abs" style="left:0;top:0" width="1200" height="1300" viewBox="0 0 1200 1300">
  <defs>
    <linearGradient id="heroBg" x1="0" y1="0" x2="0" y2="1">
      <stop offset="0" stop-color="#fdeee2"/>
      <stop offset="1" stop-color="#fff8f2"/>
    </linearGradient>
  </defs>
  <rect width="1200" height="1300" fill="url(#heroBg)"/>
  <path d="M0 920 C120 880 200 640 360 560 C520 480 600 620 700 720 C820 820 1040 800 1200 680 L1200 1300 L0 1300 Z" fill="#e7f4f5"/>
  <circle cx="-20" cy="620" r="110" fill="#fbd9bd"/>
  <circle cx="-20" cy="620" r="125" fill="none" stroke="#f6c9a3" stroke-dasharray="3 5"/>
</svg>

<div class="brand" style="left:88px;top:30px;font-size:22px"><span class="dot" style="width:26px;height:26px"></span>LARKFIELD</div>
<nav class="nav"><span class="active">HOME</span><span>SERVICES</span><span>JOIN OUR TEAM</span><span>ABOUT US</span><span>NEWS FEED</span><span>CONTACT US</span></nav>
<div class="btn-outline" style="left:968px;top:30px;width:141px;height:30px">SERVICE REQUEST</div>

<h1 class="abs" style="left:89px;top:296px;font-size:41px;font-weight:600;line-height:44px">Welcome <span style="color:var(--teal)">Larkfield</span><br>Homecare provides</h1>
<p class="abs" style="left:89px;top:394px;width:440px;font-size:13px;line-height:20px;color:#6b6f7d">A range of services that are tailored to meet the patient's needs, helping them to maintain their independence and live happy and fulfilling lives.</p>
<div class="btn-outline" style="left:89px;top:468px;width:115px;height:30px">CONTACT US</div>

<svg class="abs" style="left:560px;top:110px" width="560" height="600" viewBox="560 110 560 600">
  <circle cx="847" cy="400" r="263" fill="none" stroke="#c9c9c9" stroke-dasharray="4 6"/>
  <circle cx="584" cy="405" r="23" fill="#8fd0b0"/>
  <circle cx="1026" cy="612" r="30" fill="#fdb70d"/>
</svg>
<div class="photo" role="img" aria-label="Mother lifting her smiling baby" style="left:640px;top:188px;width:414px;height:414px;border-radius:50%;background:radial-gradient(circle at 60% 40%,#e9d2c0,#b99a86)"></div>
<svg class="abs" style="left:817px;top:363px" width="62" height="62"><circle cx="31" cy="31" r="31" fill="#fff"/><path d="M25 20 L44 31 L25 42Z" fill="#f5891f"/></svg>
<div class="photo" role="img" aria-label="Mother holding a child" style="left:621px;top:154px;width:84px;height:84px;border-radius:50%;background:#d9bca6;border:3px solid #fff"></div>
<div class="photo" role="img" aria-label="Caregiver with senior" style="left:1015px;top:170px;width:74px;height:74px;border-radius:50%;background:#d7c2bd;border:3px solid #fff"></div>
<div class="photo" role="img" aria-label="Family moment" style="left:699px;top:605px;width:78px;height:78px;border-radius:50%;background:#d39057;border:3px solid #fff"></div>

<div class="form-card">
  <h2>Service request</h2>
  <div class="field" style="top:110px"><b>NAME*</b><span>Enter name</span></div>
  <div class="field" style="top:170px"><b>MOBILE NUMBER*</b><span>Enter mobile number</span></div>
  <div class="field" style="top:232px"><b>WHEN CALENDAR*</b><span>DD/MM / YYYY</span>
    <svg class="abs" style="right:6px;top:26px" width="12" height="12"><rect x="1" y="2" width="10" height="9" fill="none" stroke="#9da1ad"/><line x1="1" y1="5" x2="11" y2="5" stroke="#9da1ad"/></svg></div>
  <div class="field" style="top:293px"><b>CITY*</b><span>Enter city name</span></div>
  <div class="submit">SUBMIT REQUEST</div>
</div>

<div class="section-title" style="left:578px;top:906px">About Us</div>
<div class="abs about" style="left:583px;top:953px;width:475px">
  <p>Larkfield Homecare deliver comprehensive care to new born baby and mother, and elderly in the comfort of their own homes, we ensure that the needs of our clients and their families are at the heart of everything they do.</p>
  <p>Provide healthcare services at the comfort of home. Medical and Nursing services to patients ranging from newborn to elderly. Services are offered 24/7 and customized based on the need into hourly, daily, weekly and monthly packages.</p>
</div>
<div class="btn-outline" style="left:582px;top:1142px;width:116px;height:28px;font-size:10px">READ MORE</div>

<div class="photo" role="img" aria-label="Mother and laughing baby on a soft rug" style="left:0;top:1300px;width:1200px;height:582px;background:linear-gradient(100deg,#d8cbbf 0%,#cbb7a6 45%,#b58b6c 75%,#8d6347 100%)"></div>
<div class="service-card" style="left:242px;background:var(--teal)">
  <h3><span class="ic"></span>Home Nursing<br>Services</h3>
  <p>Looking for care, custodial care, Urinary catheterization care, Wound care, Injections, IV infusions, Vaccination or other nursing assistance?</p>
  <div class="more">LEARN MORE</div>
</div>
<div class="service-card" style="left:600px;background:var(--orange)">
  <h3><span class="ic"></span>New Born Baby And<br>Mother Care At Home</h3>
  <p>Worried about your newborn's needs? Facing issues in coping up with the initial challenges of feeding infant child and post-operative recovery?</p>
  <div class="more">LEARN MORE</div>
</div>

<div class="section-title" style="left:89px;top:1943px">Coronavirus update</div>
<div class="stat" style="left:123px"><small>New cases</small><strong>2,458</strong></div>
<div class="stat" style="left:260px"><small>New Deaths</small><strong>1,267</strong></div>
<div class="stat" style="left:389px"><small>Positivity Rate</small><strong>5.99%</strong></div>
<div class="stat" style="left:535px"><small>Active Cases</small><strong>49.105</strong></div>
<div class="stat o" style="left:684px"><small>Total Cases</small><strong>400,482</strong></div>
<div class="stat g" style="left:835px"><small>Recovered</small><strong>343,286</strong></div>
<div class="stat r" style="left:995px"><small>Total Deaths</small><strong>8,091</strong></div>
<div class="abs" style="left:89px;top:2131px;width:1021px;height:1px;background:var(--line)"></div>

<div class="section-title" style="left:89px;top:2192px">Join our Team</div>
<div class="team-card" style="left:89px"><div class="pic" role="img" aria-label="Team member portrait" style="background:#c9c9c9"></div><h4>Daniel Reyes</h4><p>Director @Brightmoor LTD.</p><div class="socials"><i></i><i></i><i></i></div></div>
<div class="team-card" style="left:347px"><div class="pic" role="img" aria-label="Team member portrait" style="background:#d2d2d2"></div><h4>Daniel Reyes</h4><p>Director @Brightmoor LTD.</p><div class="socials"><i></i><i></i><i></i></div></div>
<div class="team-card" style="left:605px"><div class="pic" role="img" aria-label="Team member portrait" style="background:#f4a3a6"></div><h4>Daniel Reyes</h4><p>Director @Brightmoor LTD.</p><div class="socials"><i></i><i></i><i></i></div></div>
<div class="team-card" style="left:863px"><div class="pic" role="img" aria-label="Team member portrait" style="background:#fdb60f"></div><h4>Daniel Reyes</h4><p>Director @Brightmoor LTD.</p><div class="socials"><i></i><i></i><i></i></div></div>

<div class="section-title" style="left:89px;top:2639px">News Feed</div>
<div class="news-big">
  <div class="photo" role="img" aria-label="Two women embracing and laughing" style="left:34px;top:32px;width:435px;height:275px;border-radius:10px;background:linear-gradient(120deg,#8f8f92,#c9c2bc)"></div>
  <div class="abs meta" style="left:34px;top:342px">17 July, 2020<em>4 min read</em></div>
  <h3 class="abs" style="left:34px;top:384px;font-family:'Roboto',sans-serif;font-size:25px;font-weight:500;line-height:32px">The Importance of Building<br>Meaningful Relationships</h3>
  <p class="abs" style="left:34px;top:466px;width:410px;font-size:11.5px;line-height:24px;color:#444;font-family:'Roboto',sans-serif">Establishing positive social relationships with friends and family is vital to a person's physical, mental and emotional health. No matter what stage of life you are in.</p>
</div>
<div class="news-small" style="top:2722px"><div class="thumb" role="img" aria-label="Father playing with child at home" style="background:#d8b99c"></div><div class="txt"><div class="meta">17 July, 2020<em>4 min read</em></div><h5>What Family Caregivers Need to Know About Medicare</h5></div></div>
<div class="news-small" style="top:2922px;background:#fff;box-shadow:0 4px 16px rgba(0,0,0,.05)"><div class="thumb" role="img" aria-label="Mother kissing newborn" style="background:#e9ded8"></div><div class="txt"><div class="meta">17 July, 2020<em>4 min read</em></div><h5>How to Start Long-term Care Planning for Seniors</h5></div></div>
<div class="news-small" style="top:3122px"><div class="thumb" role="img" aria-label="Mother cradling a sleeping baby" style="background:#c7b4ac"></div><div class="txt"><div class="meta">17 July, 2020<em>4 min read</em></div><h5>Spotting the Signs of Alzheimer's Disease</h5></div></div>

<div class="abs" style="left:330px;top:3490px;width:780px;height:421px;background:var(--teal)"></div>
<div class="abs" style="left:188px;top:3853px;width:142px;height:58px;background:var(--teal)"></div>
<div class="photo" role="img" aria-label="Mother and baby lying on white bedding" style="left:89px;top:3373px;width:488px;height:321px;background:linear-gradient(120deg,#eef2f6,#d9c6b6)"></div>
<div class="abs" style="left:89px;top:3694px;width:488px;height:159px;background:var(--orange);color:#fff;text-align:center">
  <p style="margin-top:50px;font-size:21px;line-height:27px">"Your clients usually know their<br>field better than you do"</p>
  <p style="margin-top:8px;font-size:16px;font-weight:500">DANIEL REYES</p>
</div>
<svg class="abs" style="left:301px;top:3653px" width="64" height="64"><circle cx="32" cy="32" r="32" fill="#fff"/><text x="32" y="44" text-anchor="middle" font-family="Poppins,sans-serif" font-size="32" font-weight="700" fill="#f5891f">"</text></svg>
<div class="abs" style="left:652px;top:3603px;width:390px;color:#fff">
  <h2 style="font-size:33px;font-weight:500">Testimonials</h2>
  <p style="margin-top:6px;font-size:14px;line-height:23px">Lorem Ipsum is simply dummy text of the printing and typesetting industry. Lorem Ipsum has been the industry's standard dummy text ever since the 1500s, when ...</p>
  <div style="display:flex;align-items:center;gap:14px;margin-top:8px"><span style="font-size:37px;font-weight:500">70+</span><span style="font-size:12px;line-height:15px">Happy<br>Customers</span></div>
</div>

<div class="abs" style="left:0;top:4096px;width:1200px;height:425px;background:var(--soft)"></div>
<div class="abs" style="left:89px;top:4022px;width:1021px;height:118px;background:#fff;box-shadow:0 6px 24px rgba(0,0,0,.06)"></div>
<div class="section-title" style="left:120px;top:4062px">Get in touch with us</div>
<div class="btn-fill" style="left:895px;top:4066px;width:166px;height:37px;font-size:15px">CONTACT US</div>

<footer>
  <div class="brand" style="left:88px;top:4292px;font-size:28px"><span class="dot" style="width:34px;height:34px"></span>LARKFIELD</div>
  <div class="abs" style="left:388px;top:4231px"><h6>Useful Links</h6><ul><li>Services</li><li>Contact Us</li><li>Join our Team</li><li>About us</li><li>News Feed</li><li>Service request</li></ul></div>
  <div class="abs" style="left:591px;top:4231px;width:220px"><h6>Newsletter</h6><p class="note">Subscribe to our newsletter</p>
    <div style="margin-top:8px;height:26px;background:#fff;font-size:11px;color:#8a8f9c;padding:5px 12px;font-family:Roboto,sans-serif">Enter email address</div>
    <div class="btn-fill" style="position:relative;margin-top:10px;width:106px;height:28px;font-size:10px">SUBSCRIBE</div></div>
  <div class="abs" style="left:874px;top:4231px"><h6>Contact Us</h6>
    <ul>
      <li><span style="color:var(--teal)">●</span> Some goes adress here</li>
      <li><span style="color:var(--teal)">■</span> hello@larkfieldcare.com</li>
      <li><span style="color:var(--teal)">●</span> 555 01234 567</li>
      <li><span style="color:var(--teal)">■</span> 555 01234 567</li>
    </ul>
    <div style="display:flex;gap:8px;margin-top:6px"><i class="ring"></i><i class="ring"></i><i class="ring"></i><i class="ring"></i></div>
  </div>
  <div class="abs" style="left:89px;top:4464px;width:1021px;height:1px;background:#dcdde1"></div>
  <svg class="abs" style="left:1125px;top:4447px" width="34" height="34"><circle cx="17" cy="17" r="17" fill="#15a1a8"/><path d="M11 20 L17 14 L23 20" stroke="#fff" stroke-width="2" fill="none"/></svg>
  <p class="abs" style="left:0;top:4482px;width:1200px;text-align:center;font-size:15px;font-weight:500">©Copyright 2021 | All Rights Reserved</p>
</footer>
</body>
</html>
```